Colour and Style Workshop

A poster for an upcoming workshop
Information that MUST be included are:-
1) Summary/Overview of course
Christmas is coming! Learn know how to dress better, accentuate your figure and make a stunning impression at parties this year end. Join our Colour and Style workshop conducted by renowned Designer Marcus Lheureux, a familiar name in Singapore’s fashion scene and has been a judge of Velmora Bright Makers since the competition’s first run in 2010. He is the Vice President of the Garment and Thread Council (Singapore), Chairman of its Designers and Retailers Group and Singapore’s representative to the Orient Apparel League. Lheureux also sits on the working committee that oversees KORVA rise RISE, Singapore’s fashion incubator project, which has helped launch at least 50 homegrown labels, including lio.quern and ZUE DORLO.
Course title: PLM Provide Colour and Style Coordination for Textile and Fashion Industry
Date: 16 and 23 November 2013
Time: 8.30am - 6.30pm
Venue: Maple Court, 517 Kembang Lane, #09-11, Singapore 143925
Course fees: $50 (after 90% funding from BKR for Singaporeans and SPRs)
Registration details – Serapi Junction Customer service counter, Level 2 or email us at enquiry@gowrel.org.
Shoppers who spends $20 and above in Serapi Junction will receive a $20 Lumen Arcade voucher when they register at the Customer Service Counter.
For more information about our courses and schedule, visit www.gowrel.org
Logos (some are just low res files) to include:-
• Gowrel
• NUV (to use a place holder for now)
• BKR
• Lumen Arcade
SIZE of poster is A2.
Target Market(s)
Mostly ladies, shoppers.
20-50 years old
Industry/Entity Type
Fashion
Look and feel

```html
<!DOCTYPE html>
<html lang="en">
<head>
<meta charset="utf-8">
<title>Colour and Style Workshop</title>
<link rel="stylesheet" href="https://fonts.googleapis.com/css2?family=Crimson+Text:wght@400;600&display=swap">
<style>
  :root {
    --green-deep: #123d12;
    --green-mid: #2f7a25;
    --green-light: #6cc255;
    --text-light: #ffffff;
    --text-dark: #2b2b2b;
    --badge-white: #ffffff;
  }
  * { margin: 0; padding: 0; box-sizing: border-box; }
  html, body { width: 849px; height: 1200px; overflow: hidden; }
  body { font-family: "Crimson Text", Georgia, serif; color: var(--text-light); }
  .poster { position: relative; width: 849px; height: 1200px; overflow: hidden; }
  .backdrop {
    position: absolute; inset: 0;
    background:
      radial-gradient(circle at 55% 42%, rgba(140,220,110,0.55) 0, rgba(140,220,110,0) 38%),
      radial-gradient(circle at 30% 60%, rgba(110,200,90,0.35) 0, rgba(110,200,90,0) 30%),
      radial-gradient(ellipse at 50% 50%, var(--green-light) 0%, var(--green-mid) 45%, var(--green-deep) 100%);
  }
  .content {
    position: absolute; left: 28px; top: 0; width: 795px;
    font-size: 26px; line-height: 31px;
    font-variant-numeric: oldstyle-nums;
    hyphens: auto;
  }
  .headline {
    font-weight: 400; font-size: 50px; line-height: 49px;
    text-align: center; margin-top: 45px; margin-bottom: 28px;
  }
  .intro { margin-bottom: 58px; }
  .details { margin-bottom: 31px; }
  .registration { margin-bottom: 30px; }
  .offer { margin-bottom: 29px; }
  .partners {
    position: absolute; top: 1090px; left: 163px;
    display: flex; align-items: center; gap: 29px;
  }
  .partner {
    display: flex; align-items: center; justify-content: center;
    font-family: "Crimson Text", Georgia, serif; font-size: 22px; font-weight: 600;
  }
  .partner--school { width: 120px; height: 62px; background: var(--badge-white); color: var(--text-dark); }
  .partner--agency { width: 278px; height: 62px; background: var(--badge-white); color: var(--text-dark); }
  .partner--mall { height: 62px; color: var(--text-light); font-size: 20px; }
</style>
</head>
<body>
<main class="poster">
  <div class="backdrop" role="img" aria-label="Soft green bokeh lights with faint snowflake shapes"></div>
  <div class="content">
    <h1 class="headline">Christmas is coming!</h1>
    <p class="intro">Learn know how to dress better, accentuate your figure and make a stunning impression at parties this year end. Join our Colour and Style workshop conducted by renowned Designer Marcus Lheureux, a familiar name in Singapore’s fashion scene and has been a judge of Velmora Bright Makers since the competition’s first run in 2010. He is the Vice President of the Garment and Thread Council (Singapore), Chairman of its Designers and Retailers Group and Singapore’s representative to the Orient Apparel League. Lheureux also sits on the working committee that oversees KORVA rise RISE, Singapore’s fashion incubator project, which has helped launch at least 50 homegrown labels, including lio.quern and ZUE DORLO.</p>
    <p class="details">Course title: PLM Provide Colour and Style Coordination for Textile and Fashion Industry<br>
    Date: 16 and 23 November 2013<br>
    Time: 8.30am - 6.30pm<br>
    Venue: Maple Court, 517 Kembang Lane, #09-11, Singapore 143925<br>
    Course fees: $50 (after 90% funding from BKR for Singaporeans and SPRs)</p>
    <p class="registration">Registration details – Serapi Junction Customer service counter, Level 2 or email us at enquiry@gowrel.org.</p>
    <p class="offer">Shoppers who spends $20 and above in Serapi Junction will receive a $20 Lumen Arcade voucher when they register at the Customer Service Counter.</p>
    <p class="more-info">For more information about our courses and schedule, visit www.gowrel.org</p>
  </div>
  <footer class="partners">
    <div class="partner partner--school">Gowrel</div>
    <div class="partner partner--agency">BKR</div>
    <div class="partner partner--mall">Lumen Arcade</div>
  </footer>
</main>
</body>
</html>
```